New landing page

We have an existing design at www.hostqubit.com but we are not set on that design and probably want something different.
We want to increase conversion rates and experiment with a new landing page for our lumo bidclick campains.
We want to use a more single page long design page that contains these elements on one page:

Header
Images/headline
4 offer boxes
Features
Locations (map)
Testimonials
Why HostQubit
Footer menu

Note should also be taken of research done by Fernlatch like this:
http://fernlatch.com/landing-page-articles/the-anatomy-of-a-landing-page/

```html
<!DOCTYPE html>
<html lang="en">
<head>
<meta charset="utf-8">
<title>HostQubit — VPS Hosting</title>
<link rel="stylesheet" href="https://fonts.googleapis.com/css2?family=Open+Sans:ital,wght@0,400;0,600;0,700;0,800;1,400&display=swap">
<style>
:root{
  --orange:#f7941d;
  --orange-deep:#ef8a0f;
  --yellow:#fdd55c;
  --yellow-btn:#e8b73a;
  --cream:#fcf3dc;
  --peach:#fde8cb;
  --dark:#2b2b2b;
  --ink:#333333;
  --grey:#777777;
  --panel:#f8f8f8;
  --line:#e2e2e2;
  --quote-bg:#e7e7e7;
  --footer:#1f222a;
  --footer-low:#15171d;
  --map:#dfe3d6;
}
*{box-sizing:border-box;margin:0;padding:0}
html,body{width:1200px;height:900px;overflow:hidden}
body{font-family:"Open Sans",Arial,sans-serif;color:var(--ink);background:#fff;position:relative}
.abs{position:absolute}

/* header */
.topbar{left:0;top:0;width:1200px;height:31px;border-top:2px solid var(--orange);background:#fff}
.brand{left:170px;top:5px;display:flex;align-items:center;gap:8px;font-size:18px;font-weight:600;color:var(--orange);letter-spacing:1px}
.brand-dot{width:18px;height:18px;border-radius:50%;background:var(--orange)}
.account{right:165px;top:3px;font-size:7px;color:var(--ink)}
.phone{right:165px;top:12px;font-size:10px;color:var(--ink);display:flex;align-items:center;gap:10px}
.phone svg{width:11px;height:11px}

.nav{left:0;top:31px;width:1200px;height:13px;background:var(--dark)}
.nav ul{list-style:none;display:flex;position:absolute;left:187px;top:0;height:13px}
.nav li{font-size:7px;color:#ddd;text-transform:uppercase;line-height:13px;padding:0 18px}
.nav li.active{background:var(--orange);color:#fff}

/* hero */
.hero{left:0;top:44px;width:1200px;height:111px;background:var(--yellow)}
.hero-art{left:118px;top:8px;width:437px;height:83px;background:var(--cream);border-radius:60px 60px 30px 30px}
.hero-arrow{top:38px;width:24px;height:26px}
.hero-title{left:580px;top:9px;font-size:17px;color:var(--ink);letter-spacing:.5px;font-weight:400}
.hero-mark{left:580px;top:29px;font-size:14px;font-weight:800;color:#fff;background:var(--ink);padding:0 4px;line-height:15px;letter-spacing:1px}
.hero-sub{left:583px;top:47px;font-size:13px;font-weight:700;line-height:13px;color:var(--ink);width:360px}
.hero-btn{left:583px;top:78px;width:144px;height:14px;background:var(--yellow-btn);font-size:7px;text-align:center;line-height:14px;color:var(--ink);text-transform:uppercase}

/* feature boxes */
.feature{top:172px;width:278px;height:103px;background:var(--panel);border-bottom:1px solid var(--line);text-align:center}
.feature-icon{margin:8px auto 0;width:70px;height:34px;border-radius:50%;background:#fff;border:1px solid #eee;display:flex;align-items:center;justify-content:center}
.feature-icon.solid{background:var(--orange);border-color:var(--orange)}
.feature h3{font-size:10px;font-weight:700;color:var(--orange);margin-top:5px;text-transform:uppercase}
.feature p{font-size:8px;color:var(--grey);line-height:9px;width:245px;margin:2px auto 0}
.feature .more{font-size:7px;color:var(--ink);margin-top:9px}

/* pricing */
.pricing{left:0;top:292px;width:1200px;height:228px;background:var(--peach)}
.section-title{width:1200px;text-align:center;font-size:20px;font-weight:400;letter-spacing:1px;color:var(--ink);text-transform:uppercase}
.pricing-intro{left:280px;top:40px;width:640px;text-align:center;font-size:7px;font-style:italic;line-height:8px;color:var(--ink)}
.plan{top:62px;width:204px;height:143px;background:#fff}
.plan-head{height:17px;background:var(--orange);color:#fff;font-size:10px;font-weight:700;text-align:center;line-height:17px;letter-spacing:.5px}
.plan-ram{font-size:8px;font-weight:700;text-align:center;line-height:8px;padding:1px 0 2px;border-bottom:1px solid var(--line)}
.plan-row{font-size:6.5px;color:var(--grey);text-align:center;height:12px;line-height:12px;border-bottom:1px solid var(--line)}
.plan-price{position:absolute;left:0;top:101px;width:204px;height:42px;background:var(--dark);text-align:center;color:#fff}
.plan-price .amount{font-size:22px;line-height:24px;font-weight:400}
.plan-price .amount small{font-size:14px}
.plan-price .per{font-size:6px;font-weight:700;line-height:6px}
.plan-price .order{font-size:12px;color:var(--orange-deep);line-height:13px;background:#1a1a1a;margin-top:1px}

/* tabs */
.tabs{left:165px;top:540px;width:870px;height:19px;display:flex}
.tab{width:222px;height:19px;background:#e3e3e3;display:flex;align-items:center;font-size:7.5px;font-weight:700;line-height:7px;text-transform:uppercase;color:var(--ink)}
.tab .tab-icon{width:50px;height:19px;background:#f0f0f0;display:flex;align-items:center;justify-content:center}
.tab.active .tab-icon{background:var(--dark)}
.tab.active .tab-label{background:var(--dark);color:#fff;height:19px;width:150px;display:flex;align-items:center}
.tab-label{padding-left:10px}
.perk{width:195px}
.perk h4{font-size:7.5px;font-weight:800;text-transform:uppercase;display:flex;align-items:center;gap:14px}
.perk p{font-size:7.5px;line-height:8px;margin-top:5px;color:var(--ink)}
.perk-icon{width:20px;height:11px;border:1.5px solid #e84a2a;border-radius:50%;display:flex;align-items:center;justify-content:center}
.perk-icon i{width:10px;height:4px;background:#e84a2a;border-radius:50%}

/* testimonials */
.quotes{left:0;top:672px;width:1200px;height:135px;background:var(--quote-bg)}
.quote-photo{left:527px;top:35px;width:146px;height:41px;border-radius:50%;background:linear-gradient(135deg,#6b5a4a,#3a3f4c);border:2px solid #fff}
.quote-name{top:80px;width:1200px;text-align:center;font-size:13px;font-weight:700;letter-spacing:.5px}
.quote-text{left:288px;top:98px;width:624px;text-align:center;font-size:8.5px;line-height:8px;color:var(--grey)}
.dots{left:582px;top:118px;display:flex;gap:4px}
.dots i{width:8px;height:5px;border-radius:50%;background:#fff}

/* footer */
.footer{left:0;top:807px;width:1200px;height:78px;background:var(--footer);color:#bbb}
.footer h5{font-size:7px;color:var(--orange);font-weight:600;text-transform:uppercase;letter-spacing:.5px}
.footer ul{list-style:none;font-size:7px;line-height:7px;margin-top:4px}
.footer p{font-size:7px;line-height:7px}
.footer .meta{color:#888;font-size:5.5px}
.footer .link{color:#fff;font-weight:700;font-size:7px;text-decoration:underline}
.contact-line{display:flex;align-items:center;gap:6px;font-size:6.5px;margin-top:4px}
.map{left:705px;top:24px;width:330px;height:46px;background:linear-gradient(135deg,#e6e8dc,var(--map))}
.bottombar{left:0;top:885px;width:1200px;height:15px;background:var(--footer-low);color:#bbb;font-size:6px}
.copy{left:166px;top:4px}
.social{left:878px;top:4px;display:flex;gap:7px}
.social i{width:24px;height:8px;border-radius:4px;background:var(--orange)}
</style>
</head>
<body>

<header class="abs topbar">
  <div class="abs brand"><span class="brand-dot"></span>HostQubit</div>
  <div class="abs account">My Account</div>
  <div class="abs phone">
    <svg viewBox="0 0 12 12"><circle cx="6" cy="6" r="6" fill="#333"/><path d="M4 3.2l1 .9-.5.9a4 4 0 0 0 2.5 2.5l.9-.5.9 1-.6.9C5.6 8.7 3.3 6.4 3.1 3.8z" fill="#fff"/></svg>
    <span>+1 800 555 0142</span>
  </div>
</header>

<nav class="abs nav">
  <ul>
    <li class="active">Home</li><li>Services</li><li>Features</li><li>Locations</li><li>FAQ</li><li>Payment Methods</li><li>Community</li><li>Support</li><li>About</li>
  </ul>
</nav>

<section class="abs hero">
  <svg class="abs hero-arrow" style="left:22px" viewBox="0 0 24 26"><path d="M20 2L4 13l16 11" fill="none" stroke="#fff" stroke-width="1.5"/></svg>
  <div class="abs hero-art" role="img" aria-label="Cloud illustration with stacked server documents"></div>
  <h1 class="abs hero-title">LOREM IPSUME DOLOR SIT</h1>
  <div class="abs hero-mark">LOREM IPSUM</div>
  <p class="abs hero-sub">lorem ipsume dolor sit is lorem ipsume dolor sit dummy text</p>
  <div class="abs hero-btn">View More</div>
  <svg class="abs hero-arrow" style="left:1154px" viewBox="0 0 24 26"><path d="M4 2l16 11L4 24" fill="none" stroke="#fff" stroke-width="1.5"/></svg>
</section>

<div class="abs feature" style="left:165px">
  <div class="feature-icon solid"><svg width="22" height="14" viewBox="0 0 22 14"><rect x="3" y="2" width="16" height="10" fill="#fff" transform="rotate(-12 11 7)"/></svg></div>
  <h3>Some Heading</h3>
  <p>Lorem Ipsum is simply dummy text of the printing and typesetting industry. Lorem Ipsum has been the industry's</p>
  <div class="more">[ Read More ]</div>
</div>
<div class="abs feature" style="left:461px">
  <div class="feature-icon"><svg width="22" height="14" viewBox="0 0 22 14"><ellipse cx="11" cy="7" rx="8" ry="5" fill="var(--orange)"/></svg></div>
  <h3>Some Heading</h3>
  <p>Lorem Ipsum is simply dummy text of the printing and typesetting industry. Lorem Ipsum has been the industry's</p>
  <div class="more">[ Read More ]</div>
</div>
<div class="abs feature" style="left:757px">
  <div class="feature-icon"><svg width="22" height="14" viewBox="0 0 22 14"><path d="M3 2l16 10M19 2L3 12" stroke="var(--orange)" stroke-width="3"/></svg></div>
  <h3>Some Heading</h3>
  <p>Lorem Ipsum is simply dummy text of the printing and typesetting industry. Lorem Ipsum has been the industry's</p>
  <div class="more">[ Read More ]</div>
</div>

<section class="abs pricing">
  <h2 class="abs section-title" style="left:0;top:10px">Some Heading Goes Here</h2>
  <p class="abs pricing-intro">Lorem ipsum dolor sit amet, consectetur adipiscing elit. Proin at nunc urna. Pellentesque congue enim sit amet arcu volutpat, quis viverra velit mattis. Vestibulum vel tortor.</p>

  <div class="abs plan" style="left:165px">
    <div class="plan-head">BUDGET VPS</div>
    <div class="plan-ram">256 MB<br>GUARANTEED RAM</div>
    <div class="plan-row">1x 3.4 Ghz Cores</div><div class="plan-row">10 GB Raid-10 Storage</div><div class="plan-row">300 GB Bandwidth</div><div class="plan-row">OS of your choice</div><div class="plan-row">59 second Activation</div>
    <div class="plan-price"><div class="amount"><small>$</small>10</div><div class="per">per month</div><div class="order">ORDER NOW</div></div>
  </div>
  <div class="abs plan" style="left:388px">
    <div class="plan-head">BUDGET VPS</div>
    <div class="plan-ram">256 MB<br>GUARANTEED RAM</div>
    <div class="plan-row">1x 3.4 Ghz Cores</div><div class="plan-row">10 GB Raid-10 Storage</div><div class="plan-row">300 GB Bandwidth</div><div class="plan-row">OS of your choice</div><div class="plan-row">59 second Activation</div>
    <div class="plan-price"><div class="amount"><small>$</small>10</div><div class="per">per month</div><div class="order">ORDER NOW</div></div>
  </div>
  <div class="abs plan" style="left:610px">
    <div class="plan-head">BUDGET VPS</div>
    <div class="plan-ram">256 MB<br>GUARANTEED RAM</div>
    <div class="plan-row">1x 3.4 Ghz Cores</div><div class="plan-row">10 GB Raid-10 Storage</div><div class="plan-row">300 GB Bandwidth</div><div class="plan-row">OS of your choice</div><div class="plan-row">59 second Activation</div>
    <div class="plan-price"><div class="amount"><small>$</small>10</div><div class="per">per month</div><div class="order">ORDER NOW</div></div>
  </div>
  <div class="abs plan" style="left:832px">
    <div class="plan-head">BUDGET VPS</div>
    <div class="plan-ram">256 MB<br>GUARANTEED RAM</div>
    <div class="plan-row">1x 3.4 Ghz Cores</div><div class="plan-row">10 GB Raid-10 Storage</div><div class="plan-row">300 GB Bandwidth</div><div class="plan-row">OS of your choice</div><div class="plan-row">59 second Activation</div>
    <div class="plan-price"><div class="amount"><small>$</small>10</div><div class="per">per month</div><div class="order">ORDER NOW</div></div>
  </div>
</section>

<div class="abs tabs">
  <div class="tab active"><span class="tab-icon"><svg width="12" height="12" viewBox="0 0 12 12"><circle cx="6" cy="6" r="5" fill="#fff"/><path d="M6 2v8M2 6h8" stroke="#2b2b2b" stroke-width="1.5"/></svg></span><span class="tab-label">Some Heading<br>Here</span></div>
  <div class="tab"><span class="tab-icon"><svg width="12" height="12" viewBox="0 0 12 12"><circle cx="6" cy="6" r="5" fill="#888"/><path d="M6 2v8M2 6h8" stroke="#fff" stroke-width="1.5"/></svg></span><span class="tab-label">Some Heading<br>Here</span></div>
  <div class="tab"><span class="tab-icon"><svg width="12" height="12" viewBox="0 0 12 12"><circle cx="6" cy="6" r="5" fill="#888"/><path d="M6 2v8M2 6h8" stroke="#fff" stroke-width="1.5"/></svg></span><span class="tab-label">Some Heading<br>Here</span></div>
  <div class="tab"><span class="tab-icon"><svg width="12" height="12" viewBox="0 0 12 12"><circle cx="6" cy="6" r="5" fill="#888"/><path d="M6 2v8M2 6h8" stroke="#fff" stroke-width="1.5"/></svg></span><span class="tab-label">Some Heading<br>Here</span></div>
</div>
<svg class="abs" style="left:172px;top:559px" width="16" height="6" viewBox="0 0 16 6"><path d="M0 0h16L8 6z" fill="#2b2b2b"/></svg>

<div class="abs perk" style="left:166px;top:575px"><h4><span class="perk-icon"><i></i></span>Heading Here</h4><p>Lorem ipsum dolor sit amet, consectetur adipiscing elit. Proin at nunc urna.</p></div>
<div class="abs perk" style="left:388px;top:575px"><h4><span class="perk-icon"><i></i></span>Heading Here</h4><p>Lorem ipsum dolor sit amet, consectetur adipiscing elit. Proin at nunc urna.</p></div>
<div class="abs perk" style="left:609px;top:575px"><h4><span class="perk-icon"><i></i></span>Heading Here</h4><p>Lorem ipsum dolor sit amet, consectetur adipiscing elit. Proin at nunc urna.</p></div>
<div class="abs perk" style="left:831px;top:575px"><h4><span class="perk-icon"><i></i></span>Heading Here</h4><p>Lorem ipsum dolor sit amet, consectetur adipiscing elit. Proin at nunc urna.</p></div>
<div class="abs perk" style="left:166px;top:623px"><h4><span class="perk-icon"><i></i></span>Heading Here</h4><p>Lorem ipsum dolor sit amet, consectetur adipiscing elit. Proin at nunc urna.</p></div>
<div class="abs perk" style="left:388px;top:623px"><h4><span class="perk-icon"><i></i></span>Heading Here</h4><p>Lorem ipsum dolor sit amet, consectetur adipiscing elit. Proin at nunc urna.</p></div>
<div class="abs perk" style="left:609px;top:623px"><h4><span class="perk-icon"><i></i></span>Heading Here</h4><p>Lorem ipsum dolor sit amet, consectetur adipiscing elit. Proin at nunc urna.</p></div>
<div class="abs perk" style="left:831px;top:623px"><h4><span class="perk-icon"><i></i></span>Heading Here</h4><p>Lorem ipsum dolor sit amet, consectetur adipiscing elit. Proin at nunc urna.</p></div>

<section class="abs quotes">
  <h2 class="abs section-title" style="left:0;top:6px">What Clients Says</h2>
  <div class="abs quote-photo" role="img" aria-label="Portrait photo of the client"></div>
  <div class="abs quote-name">DALE VARNIK</div>
  <p class="abs quote-text">Lorem Ipsum is simply dummy text of the printing and typesetting industry. Lorem Ipsum has been the<br>industry's standard dummy text ever since.</p>
  <div class="abs dots"><i></i><i></i><i></i></div>
</section>

<footer class="abs footer">
  <div class="abs" style="left:168px;top:8px">
    <h5>Quick Link</h5>
    <ul><li>Home</li><li>About us</li><li>Services</li><li>Blog</li><li>Packages</li><li>FAQ</li><li>Contact</li></ul>
  </div>
  <div class="abs" style="left:314px;top:8px;width:200px">
    <h5>Blog</h5>
    <p style="margin-top:4px">Lorem Ipsum has been the industry's<br>standard dummy text.</p>
    <p class="meta">- Admin User &nbsp; 12 Dec 2013</p>
    <p style="margin-top:3px">Lorem Ipsum has been the industry's<br>standard dummy text.</p>
    <p class="meta">- Admin User &nbsp; 12 Dec 2013</p>
    <p class="link" style="margin-top:2px">View More</p>
  </div>
  <div class="abs" style="left:538px;top:8px;width:150px">
    <h5>Address</h5>
    <p style="margin-top:4px">Lorem Ipsum has been the industry's standard dummy text.</p>
    <div class="contact-line"><svg width="8" height="8" viewBox="0 0 12 12"><path d="M3 1l2 2-1 1.5a5 5 0 0 0 3.5 3.5L9 7l2 2-1.5 2C5 10.5 1.5 7 1 2.5z" fill="#fff"/></svg>1111 1111</div>
    <div class="contact-line"><svg width="8" height="6" viewBox="0 0 12 9"><rect width="12" height="9" fill="#fff"/><path d="M0 0l6 5 6-5" fill="none" stroke="#1f222a"/></svg>hello@hostqubit.com</div>
  </div>
  <div class="abs map" role="img" aria-label="Map of data centre locations"></div>
</footer>

<div class="abs bottombar">
  <div class="abs copy">Copyright 2014. All Rights Reserved.</div>
  <div class="abs social"><i></i><i></i><i></i><i></i><i></i></div>
</div>

</body>
</html>
```